Visitenkarten-Design für Bewertung von Grundstücken
Zielgruppe
Ich bin Sachverständige für die Bewertung von bebauten und unbebauten Grundstücken und erstelle Verkehrswertgutachten für (überwiegend) Sylter Immobilien. Meine Zielgruppe sind die Eigentümer dieser Immobilien, die aus verschiedensten Gründen eine Wertermittlung für ihre Immobilie benötigen, z.B. wegen
steuerlichen Anlässen (Erbschaft, Übertragung, Schenkung)
Erbauseinandersetzungen / Pflichtteilsansprüchen
Ehescheidung
Kauf oder Verkauf eines Grundstücks
Vermögensaufstellung
Vormundschaftsangelegenheiten
Bewertung von Rechten und Belastungen (Wohnrecht, Nießbrauch, Erbbaurecht)
Aufgabenstellung
Ich habe mir erst kürzlich eine kleine Homepage erstellen lassen, die mir sehr gut gefällt.
www.wertgutachten-haldorf.de
Das Design der Visitenkarte sollte dazu passen und prägnant und schnörkellos sein. Mein Logo mit der Lupe sollte sich dort wiederfinden, ebenfalls die Farben. Ich bevorzuge schlichte Eleganz, eine schöne Haptik, hochwertiges Papier, evtl mit Prägedruck, da bin ich aber noch unsicher, evtl. eine matte und eine Hochglanzseite....

```html
<!DOCTYPE html>
<html lang="de">
<head>
<meta charset="utf-8">
<title>Visitenkarte Sachverständigenbüro Haldorf</title>
<link href="https://fonts.googleapis.com/css2?family=Open+Sans:wght@400;600;700;800&display=swap" rel="stylesheet">
<style>
  :root {
    --stage: #e6e7ea;
    --navy: #2a303d;
    --navy-deep: #1f242f;
    --navy-light: #4f5666;
    --sheen: #8a909c;
    --ink: #1c1f26;
    --grey-text: #4a4f59;
    --green: #8cc07a;
    --paper: #ffffff;
    --white: #ffffff;
    --photo-warm: #a0664a;
    --photo-mid: #7b5040;
    --photo-dark: #3a2e2a;
  }
  * { box-sizing: border-box; margin: 0; padding: 0; }
  html, body { width: 1200px; height: 977px; overflow: hidden; }
  body {
    background: var(--stage);
    font-family: "Open Sans", Arial, sans-serif;
    position: relative;
  }
  .card {
    position: absolute;
    top: 148px;
    width: 440px;
    height: 680px;
    border-radius: 26px;
    overflow: hidden;
    box-shadow: 0 10px 30px rgba(0,0,0,0.18);
  }

  /* Shared brand line */
  .brand { position: absolute; display: flex; align-items: flex-start; gap: 10px; }
  .brand-dot { width: 14px; height: 14px; border-radius: 50%; margin-top: 4px; flex: none; }
  .brand-name { font-weight: 700; font-size: 17px; letter-spacing: 0.2px; text-transform: uppercase; line-height: 1.3; }
  .brand-owner { font-weight: 600; font-size: 15px; color: var(--green); text-transform: uppercase; margin-top: 2px; line-height: 1.3; }

  /* Front */
  .card-front { left: 120px; background: var(--paper); }
  .card-front .brand { left: 36px; top: 40px; }
  .card-front .brand-dot { background: var(--ink); }
  .card-front .brand-name { color: var(--ink); }
  .person { position: absolute; left: 36px; top: 150px; }
  .person-name { font-weight: 800; font-size: 24px; color: var(--ink); text-transform: uppercase; line-height: 1.3; }
  .person-role { font-size: 15px; color: var(--grey-text); margin-top: 2px; }
  .contact { list-style: none; position: absolute; left: 36px; top: 230px; }
  .contact li { display: flex; align-items: center; gap: 10px; font-size: 16px; color: var(--ink); margin-bottom: 6px; }
  .contact svg { width: 14px; height: 14px; flex: none; }
  .portrait {
    position: absolute; left: 0; bottom: 0;
    width: 100%; height: 300px;
    background: linear-gradient(160deg, var(--photo-warm) 0%, var(--photo-mid) 45%, var(--photo-dark) 100%);
  }

  /* Back */
  .card-back { left: 640px; background: var(--navy); }
  .back-pattern {
    position: absolute; inset: 0;
    background:
      radial-gradient(ellipse 70% 45% at 45% 30%, rgba(138,144,156,0.35) 0%, rgba(138,144,156,0) 70%),
      linear-gradient(170deg, var(--navy-light) 0%, var(--navy) 45%, var(--navy-deep) 100%);
  }
  .card-back .brand { left: 48px; top: 440px; }
  .card-back .brand-dot { background: var(--white); }
  .card-back .brand-name { color: var(--white); }
</style>
</head>
<body>
  <section class="card card-front">
    <div class="brand">
      <span class="brand-dot"></span>
      <div>
        <p class="brand-name">Sachverständigenbüro Haldorf</p>
        <p class="brand-owner">Henrike Vossberg</p>
      </div>
    </div>
    <div class="person">
      <p class="person-name">Exemple Name</p>
      <p class="person-role">Director</p>
    </div>
    <ul class="contact">
      <li>
        <svg viewBox="0 0 14 14"><path d="M3 1 L5 1 L6 4 L4.5 5.5 Q6 8.5 8.5 9.5 L10 8 L13 9 L13 11 Q12 13 10 13 Q2 11 1 3 Q1 1 3 1 Z" fill="var(--green)"/></svg>
        254-000-0000
      </li>
      <li>
        <svg viewBox="0 0 14 14"><rect x="1" y="3" width="12" height="8" rx="1" fill="var(--green)"/><path d="M1.5 3.5 L7 8 L12.5 3.5" stroke="#fff" stroke-width="1.2" fill="none"/></svg>
        info@wertgutachten-haldorf.de
      </li>
      <li>
        <svg viewBox="0 0 14 14"><circle cx="7" cy="7" r="6" fill="var(--green)"/></svg>
        www.wertgutachten-haldorf.de
      </li>
    </ul>
    <div class="portrait" role="img" aria-label="Porträtfoto der Sachverständigen vor einer alten Backsteinwand"></div>
  </section>

  <section class="card card-back">
    <div class="back-pattern" role="img" aria-label="Glänzendes Wiederholungsmuster aus dem Markenzeichen auf dunklem Grund"></div>
    <div class="brand">
      <span class="brand-dot"></span>
      <div>
        <p class="brand-name">Sachverständigenbüro Haldorf</p>
        <p class="brand-owner">Henrike Vossberg</p>
      </div>
    </div>
  </section>
</body>
</html>
```